Bold, Fun Hot Sauce Label

Hello,
We are a brand that are launching 4 new flavours of Hot Sauces in the next couple of months. We're looking for a label design that is just as fun & bold as these sauces with lots of colour & a modern look. It is a 3x5 label (attached) with 4 flavours:
1. Original Hot Sauce
2. Carolina Reaper Hot Sauce
3. Trinidad Scorpion Hot Sauce
4. Ghost Pepper Hot Sauce
Thank you

```html
<!DOCTYPE html>
<html lang="en">
<head>
<meta charset="utf-8">
<title>Hot Sauce Labels</title>
<link href="https://fonts.googleapis.com/css2?family=Lilita+One&family=Mouse+Memoirs&family=Open+Sans:wght@400;600;700&display=swap" rel="stylesheet">
<style>
:root{
  --page:#e4e4e4;
  --white:#fff;
  --ghost:#be1e2d; --ghost-light:#c9414e;
  --scorpion:#e34a26; --scorpion-light:#ec7a5c;
  --reaper:#6e1a40; --reaper-light:#86395f;
  --original:#4ca20e; --original-light:#8cc63f;
}
*{margin:0;padding:0;box-sizing:border-box}
html,body{width:1200px;height:1200px;overflow:hidden;background:var(--page)}
.sheet{position:relative;width:1200px;height:1200px}
.label{position:absolute;width:560px;height:336px;background:var(--bg);color:var(--white);overflow:hidden}
.label--ghost{left:30px;top:234px;--bg:var(--ghost);--light:var(--ghost-light)}
.label--scorpion{left:610px;top:234px;--bg:var(--scorpion);--light:var(--scorpion-light)}
.label--reaper{left:30px;top:630px;--bg:var(--reaper);--light:var(--reaper-light)}
.label--original{left:610px;top:630px;--bg:var(--original);--light:var(--original-light)}
.strip{position:absolute;top:0;width:16px;height:100%;background:var(--light)}
.strip--left{left:154px}.strip--right{left:389px}
.front{position:absolute;left:170px;top:0;width:219px;height:336px}
.front svg{position:absolute;inset:0}
.fill-light{fill:var(--light)}
.brand{position:absolute;top:28px;width:100%;text-align:center;font:400 17px/1 "Lilita One",sans-serif;letter-spacing:.5px;color:var(--white)}
.product{position:absolute;top:60px;width:100%;text-align:center;font:400 47px/0.94 "Lilita One",sans-serif;letter-spacing:.5px;color:var(--white)}
.weight{position:absolute;top:166px;width:100%;text-align:center;font:400 7px/1 "Open Sans",sans-serif;color:var(--white)}
.flavour{position:absolute;top:264px;width:100%;text-align:center;font:400 34px/0.88 "Mouse Memoirs",sans-serif;letter-spacing:1.5px;color:var(--white)}
.flavour--single{top:287px}
.facts{position:absolute;top:72px;font-family:"Open Sans",sans-serif;color:var(--white)}
.facts--nutrition{left:8px;width:140px}
.facts--supplement{left:412px;width:143px}
.facts__title{font-size:13.5px;line-height:1;margin-bottom:3px}
.facts--nutrition .facts__title{font-weight:700;text-align:center}
.facts--supplement .facts__title{font-weight:400;padding-left:4px;font-size:14.5px}
.facts__meta{font-size:4px;line-height:1.4;padding-left:2px}
.facts__table{border-top:2px solid var(--white);margin-top:2px;font-size:4.2px;line-height:1.6}
.row{display:grid;grid-template-columns:1fr 30px 10px;border-bottom:0.5px solid rgba(255,255,255,.6);padding-left:2px;white-space:nowrap}
.row span:last-child{text-align:right}
.row--head{display:flex;justify-content:space-between;padding-right:2px}
.facts--nutrition .row--head span:first-child{padding-left:34px}
.facts--supplement .row{grid-template-columns:1fr 22px 8px}
.facts--supplement .row--head{display:flex}
.facts__note{border-top:1.5px solid var(--white);margin-top:3px;padding-top:2px;font-size:4px;line-height:1.45}
.facts__note b{font-weight:700}
.facts__made{font-size:5.5px;margin-top:4px}
</style>
</head>
<body>
<svg width="0" height="0" style="position:absolute" aria-hidden="true">
  <defs>
    <linearGradient id="band-heat" x1="0" y1="0" x2="0" y2="1">
      <stop offset="0" stop-color="#f7931e"/>
      <stop offset="1" stop-color="#c1272d"/>
    </linearGradient>
    <linearGradient id="art-red" x1="0" y1="0" x2="1" y2="1"><stop offset="0" stop-color="#e0513a"/><stop offset="1" stop-color="#b8261a"/></linearGradient>
    <linearGradient id="art-green" x1="0" y1="0" x2="1" y2="1"><stop offset="0" stop-color="#9fcf5a"/><stop offset="1" stop-color="#5b9a1e"/></linearGradient>
  </defs>
</svg>

<main class="sheet">

  <section class="label label--ghost">
    <div class="facts facts--nutrition">
      <h2 class="facts__title">Nutrition Facts</h2>
      <p class="facts__meta">Serving Size: 1 Tablet<br>Servings Per Container: 60</p>
      <div class="facts__table">
        <div class="row row--head"><span>Amount Per Serving</span><span>% Daily Value</span></div>
        <div class="row"><span>Vitamin A</span><span>250 mg</span><span>*</span></div>
        <div class="row"><span>Vitamin C</span><span>150 mg</span><span>*</span></div>
        <div class="row"><span>Vitamin D</span><span>125 mg</span><span>*</span></div>
        <div class="row"><span>Vitamin E</span><span>100 mg</span><span>*</span></div>
        <div class="row"><span>Vitamin B6</span><span>50 mg</span><span>*</span></div>
        <div class="row"><span>Vitamin B12</span><span>50 mg</span><span>*</span></div>
        <div class="row"><span>Thiamin</span><span>50 mg</span><span>*</span></div>
        <div class="row"><span>Biotin</span><span>10 mcg</span><span>*</span></div>
        <div class="row"><span>Riboflavin</span><span>50 mg</span><span>*</span></div>
        <div class="row"><span>Iron</span><span>10 mcg</span><span>*</span></div>
        <div class="row"><span>Hydrochloride acid</span><span>50 mg</span><span>*</span></div>
      </div>
      <p class="facts__note">* Daily Value not established<br><b>Other Ingredients:</b> Vegetable cellulose (veggie cap), Rice Flour, Silicon Dioxide.</p>
      <p class="facts__made">Manufactured for:</p>
    </div>
    <div class="strip strip--left"></div>
    <div class="front">
      <svg viewBox="0 0 219 336" width="219" height="336">
        <path class="fill-light" d="M0 300 C60 318 90 330 100 336 H0 Z"/>
        <g class="fill-light">
          <polygon points="219,236 219,252 150,336 134,336"/>
          <polygon points="219,266 219,282 175,336 159,336"/>
          <polygon points="219,296 219,312 200,336 184,336"/>
          <polygon points="160,270 176,262 120,336 104,336" opacity=".6"/>
        </g>
        <path fill="#fff" d="M0 150 H219 V195 C212 240 150 262 60 262 C30 262 10 260 0 258 Z"/>
        <path fill="#000" d="M0 0 H219 V148 Q219 185 182 185 H40 Q0 185 0 148 Z"/>
        <path fill="url(#band-heat)" d="M0 10 H219 V50 C180 62 140 42 90 50 C50 56 20 58 0 52 Z"/>
        <rect role="img" aria-label="Photograph of a red ghost pepper" x="54" y="200" width="112" height="38" rx="8" fill="url(#art-red)"/>
      </svg>
      <div class="brand">name</div>
      <div class="product">HOT<br>SAUCE</div>
      <div class="weight">NET WT 8 OZ (227g)</div>
      <div class="flavour">GHOST<br>PEPPER</div>
    </div>
    <div class="strip strip--right"></div>
    <div class="facts facts--supplement">
      <h2 class="facts__title">Supplement Facts</h2>
      <p class="facts__meta">Serving Size: 1 Vegetable Capsule<br>Servings Per Container: 60</p>
      <div class="facts__table">
        <div class="row row--head"><span>Amount Per Serving</span><span>% Daily Value</span></div>
        <div class="row"><span>St. John's Wort (as .3% hypericine)</span><span>250 mg</span><span>*</span></div>
        <div class="row"><span>Glutamine (as L-glutamine hydrochloride)</span><span>150 mg</span><span>*</span></div>
        <div class="row"><span>Phosphatidylserine Complex</span><span>125 mg</span><span>*</span></div>
        <div class="row"><span>Bacopa monnieri (Standardized to 20%)</span><span>100 mg</span><span>*</span></div>
        <div class="row"><span>DMAE Bitartrate</span><span>50 mg</span><span>*</span></div>
        <div class="row"><span>N-Acetyl-L-Carnitine HCl</span><span>50 mg</span><span>*</span></div>
        <div class="row"><span>Ginkgo biloba (Standardized to 24%)</span><span>50 mg</span><span>*</span></div>
        <div class="row"><span>Huperzine-A</span><span>10 mcg</span><span>*</span></div>
      </div>
      <p class="facts__note">* Daily Value not established<br><b>Other Ingredients:</b> Vegetable cellulose (veggie cap), Rice Flour, Silicon Dioxide.</p>
      <p class="facts__made">Manufactured for:</p>
    </div>
  </section>

  <section class="label label--scorpion">
    <div class="facts facts--nutrition">
      <h2 class="facts__title">Nutrition Facts</h2>
      <p class="facts__meta">Serving Size: 1 Tablet<br>Servings Per Container: 60</p>
      <div class="facts__table">
        <div class="row row--head"><span>Amount Per Serving</span><span>% Daily Value</span></div>
        <div class="row"><span>Vitamin A</span><span>250 mg</span><span>*</span></div>
        <div class="row"><span>Vitamin C</span><span>150 mg</span><span>*</span></div>
        <div class="row"><span>Vitamin D</span><span>125 mg</span><span>*</span></div>
        <div class="row"><span>Vitamin E</span><span>100 mg</span><span>*</span></div>
        <div class="row"><span>Vitamin B6</span><span>50 mg</span><span>*</span></div>
        <div class="row"><span>Vitamin B12</span><span>50 mg</span><span>*</span></div>
        <div class="row"><span>Thiamin</span><span>50 mg</span><span>*</span></div>
        <div class="row"><span>Biotin</span><span>10 mcg</span><span>*</span></div>
        <div class="row"><span>Riboflavin</span><span>50 mg</span><span>*</span></div>
        <div class="row"><span>Iron</span><span>10 mcg</span><span>*</span></div>
        <div class="row"><span>Hydrochloride acid</span><span>50 mg</span><span>*</span></div>
      </div>
      <p class="facts__note">* Daily Value not established<br><b>Other Ingredients:</b> Vegetable cellulose (veggie cap), Rice Flour, Silicon Dioxide.</p>
      <p class="facts__made">Manufactured for:</p>
    </div>
    <div class="strip strip--left"></div>
    <div class="front">
      <svg viewBox="0 0 219 336" width="219" height="336">
        <path class="fill-light" d="M0 300 C60 318 90 330 100 336 H0 Z"/>
        <g class="fill-light">
          <polygon points="219,236 219,252 150,336 134,336"/>
          <polygon points="219,266 219,282 175,336 159,336"/>
          <polygon points="219,296 219,312 200,336 184,336"/>
          <polygon points="160,270 176,262 120,336 104,336" opacity=".6"/>
        </g>
        <path fill="#fff" d="M0 150 H219 V195 C212 240 150 262 60 262 C30 262 10 260 0 258 Z"/>
        <path fill="#000" d="M0 0 H219 V148 Q219 185 182 185 H40 Q0 185 0 148 Z"/>
        <path fill="url(#band-heat)" d="M0 10 H219 V50 C180 62 140 42 90 50 C50 56 20 58 0 52 Z"/>
        <rect role="img" aria-label="Photograph of a red Trinidad scorpion pepper" x="84" y="194" width="56" height="52" rx="8" fill="url(#art-red)"/>
      </svg>
      <div class="brand">name</div>
      <div class="product">HOT<br>SAUCE</div>
      <div class="weight">NET WT 8 OZ (227g)</div>
      <div class="flavour">TRINIDAD<br>SCORPION</div>
    </div>
    <div class="strip strip--right"></div>
    <div class="facts facts--supplement">
      <h2 class="facts__title">Supplement Facts</h2>
      <p class="facts__meta">Serving Size: 1 Vegetable Capsule<br>Servings Per Container: 60</p>
      <div class="facts__table">
        <div class="row row--head"><span>Amount Per Serving</span><span>% Daily Value</span></div>
        <div class="row"><span>St. John's Wort (as .3% hypericine)</span><span>250 mg</span><span>*</span></div>
        <div class="row"><span>Glutamine (as L-glutamine hydrochloride)</span><span>150 mg</span><span>*</span></div>
        <div class="row"><span>Phosphatidylserine Complex</span><span>125 mg</span><span>*</span></div>
        <div class="row"><span>Bacopa monnieri (Standardized to 20%)</span><span>100 mg</span><span>*</span></div>
        <div class="row"><span>DMAE Bitartrate</span><span>50 mg</span><span>*</span></div>
        <div class="row"><span>N-Acetyl-L-Carnitine HCl</span><span>50 mg</span><span>*</span></div>
        <div class="row"><span>Ginkgo biloba (Standardized to 24%)</span><span>50 mg</span><span>*</span></div>
        <div class="row"><span>Huperzine-A</span><span>10 mcg</span><span>*</span></div>
      </div>
      <p class="facts__note">* Daily Value not established<br><b>Other Ingredients:</b> Vegetable cellulose (veggie cap), Rice Flour, Silicon Dioxide.</p>
      <p class="facts__made">Manufactured for:</p>
    </div>
  </section>

  <section class="label label--reaper">
    <div class="facts facts--nutrition">
      <h2 class="facts__title">Nutrition Facts</h2>
      <p class="facts__meta">Serving Size: 1 Tablet<br>Servings Per Container: 60</p>
      <div class="facts__table">
        <div class="row row--head"><span>Amount Per Serving</span><span>% Daily Value</span></div>
        <div class="row"><span>Vitamin A</span><span>250 mg</span><span>*</span></div>
        <div class="row"><span>Vitamin C</span><span>150 mg</span><span>*</span></div>
        <div class="row"><span>Vitamin D</span><span>125 mg</span><span>*</span></div>
        <div class="row"><span>Vitamin E</span><span>100 mg</span><span>*</span></div>
        <div class="row"><span>Vitamin B6</span><span>50 mg</span><span>*</span></div>
        <div class="row"><span>Vitamin B12</span><span>50 mg</span><span>*</span></div>
        <div class="row"><span>Thiamin</span><span>50 mg</span><span>*</span></div>
        <div class="row"><span>Biotin</span><span>10 mcg</span><span>*</span></div>
        <div class="row"><span>Riboflavin</span><span>50 mg</span><span>*</span></div>
        <div class="row"><span>Iron</span><span>10 mcg</span><span>*</span></div>
        <div class="row"><span>Hydrochloride acid</span><span>50 mg</span><span>*</span></div>
      </div>
      <p class="facts__note">* Daily Value not established<br><b>Other Ingredients:</b> Vegetable cellulose (veggie cap), Rice Flour, Silicon Dioxide.</p>
      <p class="facts__made">Manufactured for:</p>
    </div>
    <div class="strip strip--left"></div>
    <div class="front">
      <svg viewBox="0 0 219 336" width="219" height="336">
        <path class="fill-light" d="M0 300 C60 318 90 330 100 336 H0 Z"/>
        <g class="fill-light">
          <polygon points="219,236 219,252 150,336 134,336"/>
          <polygon points="219,266 219,282 175,336 159,336"/>
          <polygon points="219,296 219,312 200,336 184,336"/>
          <polygon points="160,270 176,262 120,336 104,336" opacity=".6"/>
        </g>
        <path fill="#fff" d="M0 150 H219 V195 C212 240 150 262 60 262 C30 262 10 260 0 258 Z"/>
        <path fill="#000" d="M0 0 H219 V148 Q219 185 182 185 H40 Q0 185 0 148 Z"/>
        <path fill="url(#band-heat)" d="M0 10 H219 V50 C180 62 140 42 90 50 C50 56 20 58 0 52 Z"/>
        <rect role="img" aria-label="Photograph of a red Carolina reaper pepper" x="72" y="196" width="84" height="46" rx="8" fill="url(#art-red)"/>
      </svg>
      <div class="brand">name</div>
      <div class="product">HOT<br>SAUCE</div>
      <div class="weight">NET WT 8 OZ (227g)</div>
      <div class="flavour">CAROLINA<br>REAPER</div>
    </div>
    <div class="strip strip--right"></div>
    <div class="facts facts--supplement">
      <h2 class="facts__title">Supplement Facts</h2>
      <p class="facts__meta">Serving Size: 1 Vegetable Capsule<br>Servings Per Container: 60</p>
      <div class="facts__table">
        <div class="row row--head"><span>Amount Per Serving</span><span>% Daily Value</span></div>
        <div class="row"><span>St. John's Wort (as .3% hypericine)</span><span>250 mg</span><span>*</span></div>
        <div class="row"><span>Glutamine (as L-glutamine hydrochloride)</span><span>150 mg</span><span>*</span></div>
        <div class="row"><span>Phosphatidylserine Complex</span><span>125 mg</span><span>*</span></div>
        <div class="row"><span>Bacopa monnieri (Standardized to 20%)</span><span>100 mg</span><span>*</span></div>
        <div class="row"><span>DMAE Bitartrate</span><span>50 mg</span><span>*</span></div>
        <div class="row"><span>N-Acetyl-L-Carnitine HCl</span><span>50 mg</span><span>*</span></div>
        <div class="row"><span>Ginkgo biloba (Standardized to 24%)</span><span>50 mg</span><span>*</span></div>
        <div class="row"><span>Huperzine-A</span><span>10 mcg</span><span>*</span></div>
      </div>
      <p class="facts__note">* Daily Value not established<br><b>Other Ingredients:</b> Vegetable cellulose (veggie cap), Rice Flour, Silicon Dioxide.</p>
      <p class="facts__made">Manufactured for:</p>
    </div>
  </section>

  <section class="label label--original">
    <div class="facts facts--nutrition">
      <h2 class="facts__title">Nutrition Facts</h2>
      <p class="facts__meta">Serving Size: 1 Tablet<br>Servings Per Container: 60</p>
      <div class="facts__table">
        <div class="row row--head"><span>Amount Per Serving</span><span>% Daily Value</span></div>
        <div class="row"><span>Vitamin A</span><span>250 mg</span><span>*</span></div>
        <div class="row"><span>Vitamin C</span><span>150 mg</span><span>*</span></div>
        <div class="row"><span>Vitamin D</span><span>125 mg</span><span>*</span></div>
        <div class="row"><span>Vitamin E</span><span>100 mg</span><span>*</span></div>
        <div class="row"><span>Vitamin B6</span><span>50 mg</span><span>*</span></div>
        <div class="row"><span>Vitamin B12</span><span>50 mg</span><span>*</span></div>
        <div class="row"><span>Thiamin</span><span>50 mg</span><span>*</span></div>
        <div class="row"><span>Biotin</span><span>10 mcg</span><span>*</span></div>
        <div class="row"><span>Riboflavin</span><span>50 mg</span><span>*</span></div>
        <div class="row"><span>Iron</span><span>10 mcg</span><span>*</span></div>
        <div class="row"><span>Hydrochloride acid</span><span>50 mg</span><span>*</span></div>
      </div>
      <p class="facts__note">* Daily Value not established<br><b>Other Ingredients:</b> Vegetable cellulose (veggie cap), Rice Flour, Silicon Dioxide.</p>
      <p class="facts__made">Manufactured for:</p>
    </div>
    <div class="strip strip--left"></div>
    <div class="front">
      <svg viewBox="0 0 219 336" width="219" height="336">
        <path class="fill-light" d="M0 300 C60 318 90 330 100 336 H0 Z"/>
        <g class="fill-light">
          <polygon points="219,236 219,252 150,336 134,336"/>
          <polygon points="219,266 219,282 175,336 159,336"/>
          <polygon points="219,296 219,312 200,336 184,336"/>
          <polygon points="160,270 176,262 120,336 104,336" opacity=".6"/>
        </g>
        <path fill="#fff" d="M0 150 H219 V195 C212 240 150 262 60 262 C30 262 10 260 0 258 Z"/>
        <path fill="#000" d="M0 0 H219 V148 Q219 185 182 185 H40 Q0 185 0 148 Z"/>
        <path fill="url(#band-heat)" d="M0 10 H219 V50 C180 62 140 42 90 50 C50 56 20 58 0 52 Z"/>
        <rect role="img" aria-label="Photograph of a green chili pepper" x="40" y="198" width="140" height="40" rx="8" fill="url(#art-green)"/>
      </svg>
      <div class="brand">name</div>
      <div class="product">HOT<br>SAUCE</div>
      <div class="weight">NET WT 8 OZ (227g)</div>
      <div class="flavour flavour--single">ORIGINAL</div>
    </div>
    <div class="strip strip--right"></div>
    <div class="facts facts--supplement">
      <h2 class="facts__title">Supplement Facts</h2>
      <p class="facts__meta">Serving Size: 1 Vegetable Capsule<br>Servings Per Container: 60</p>
      <div class="facts__table">
        <div class="row row--head"><span>Amount Per Serving</span><span>% Daily Value</span></div>
        <div class="row"><span>St. John's Wort (as .3% hypericine)</span><span>250 mg</span><span>*</span></div>
        <div class="row"><span>Glutamine (as L-glutamine hydrochloride)</span><span>150 mg</span><span>*</span></div>
        <div class="row"><span>Phosphatidylserine Complex</span><span>125 mg</span><span>*</span></div>
        <div class="row"><span>Bacopa monnieri (Standardized to 20%)</span><span>100 mg</span><span>*</span></div>
        <div class="row"><span>DMAE Bitartrate</span><span>50 mg</span><span>*</span></div>
        <div class="row"><span>N-Acetyl-L-Carnitine HCl</span><span>50 mg</span><span>*</span></div>
        <div class="row"><span>Ginkgo biloba (Standardized to 24%)</span><span>50 mg</span><span>*</span></div>
        <div class="row"><span>Huperzine-A</span><span>10 mcg</span><span>*</span></div>
      </div>
      <p class="facts__note">* Daily Value not established<br><b>Other Ingredients:</b> Vegetable cellulose (veggie cap), Rice Flour, Silicon Dioxide.</p>
      <p class="facts__made">Manufactured for:</p>
    </div>
  </section>

</main>
</body>
</html>
```